Insurance Firm needs Stationary and Corporate Identity

We have a logo (provided) - we need a business card, letterhead, booklet cover, Benefit & Travel card design, and brand guide.
KTR (Kestrel Trust Reinsurers) is a National (Canadian) family-run benefits firm. We've been providing alternative benefit models to small and medium sized businesses for almost 25 years! Our goal is to create long-lasting customer relationships by partnering with our clients to become their dedicated benefits division instead of just selling a product to them.

Benefit & Travel Cards: We provide the benefit card to employees to allow them to pay for drugs at their pharmacy and dental services electronically.
The travel card is for medical emergencies while travelling outside of Canada.

Brand Guide: Once the stationary is complete, the brand guide will allow us to streamline the use of our logo's and fonts for internal and external use. We will expect that this will be a paid project for our design winner after the contest closes and we will negotiate the pricetag for this at that time.

Target Market(s)

Business Owners, Entrepreneurs, HR Professionals

Industry/Entity Type

Insurance Agency

Font styles to use
Sans Serif

Requirements
Must have
• business card, letterhead, health card, travel card, booklet cover (some current samples provided)

```html
<!DOCTYPE html>
<html lang="en">
<head>
<meta charset="utf-8">
<title>Kestrel Trust Reinsurers — Stationery Suite</title>
<link href="https://fonts.googleapis.com/css2?family=Lato:wght@400;700;900&family=Montserrat:wght@500;600;700;800&display=swap" rel="stylesheet">
<style>
  :root{
    --red:#e0262b;
    --red-deep:#c91c22;
    --grey:#808285;
    --grey-light:#b5b7ba;
    --board:#ebebeb;
    --paper:#ffffff;
    --ink:#333333;
  }
  *{margin:0;padding:0;box-sizing:border-box}
  html,body{width:1200px;height:898px;overflow:hidden;background:var(--board)}
  body{position:relative;font-family:"Lato",sans-serif;color:var(--ink)}
  .piece{position:absolute;overflow:hidden;background:var(--paper);box-shadow:0 2px 6px rgba(0,0,0,.22)}
  .piece > svg{position:absolute;inset:0;width:100%;height:100%}
  .label{position:absolute;font-family:"Montserrat",sans-serif;font-weight:500;font-size:15px;color:#222;letter-spacing:.3px;transform:translateX(-50%);white-space:nowrap}
  .abs{position:absolute;white-space:nowrap}

  /* Booklet */
  .booklet{left:22px;top:26px;width:436px;height:588px}
  .booklet .brand{left:52px;top:34px;font-family:"Lato",sans-serif;font-weight:700;font-size:72px;color:var(--grey);letter-spacing:2px}
  .booklet .title{left:140px;top:500px;width:290px;text-align:center;font-family:"Montserrat",sans-serif;font-weight:800;font-size:26px;color:#fff}
  .booklet .tagline{left:140px;top:532px;width:290px;text-align:center;font-family:"Montserrat",sans-serif;font-weight:500;font-size:9.5px;color:#fff;letter-spacing:.3px}

  /* Letterhead */
  .letterhead{left:498px;top:26px;width:416px;height:588px}
  .letterhead .brand{left:22px;top:30px;font-weight:700;font-size:27px;color:var(--grey)}
  .contact{font-family:"Montserrat",sans-serif;font-weight:600;font-size:8px;color:#fff;display:flex;align-items:center;gap:5px}
  .contact i{display:inline-block;width:8px;height:8px;border-radius:50%;background:#fff}
  .letterhead .meta{font-size:7.5px;color:#222}
  .letterhead .body{left:20px;width:376px;white-space:normal;font-size:6.4px;line-height:12.4px;color:#444;text-align:justify;text-indent:20px}
  .letterhead .foot{left:0;top:561px;width:416px;justify-content:center}

  /* Cards */
  .card{width:229px;height:138px}
  .card.health{left:950px;top:26px}
  .card.travel{left:950px;top:233px}
  .card.front{left:22px;top:693px}
  .card.back{left:288px;top:693px;background:#f1f1f1}
  .card .brand{font-weight:700;font-size:28px;color:var(--grey);letter-spacing:1px}
  .card .sub{font-size:6.4px;font-weight:700;color:var(--red);letter-spacing:.2px}
  .card .sub2{font-size:5px;color:var(--grey);letter-spacing:.6px}
  .card .lines{font-size:3.8px;line-height:8.8px;color:#fff;font-weight:700}
  .card .lines span{display:flex;align-items:center;gap:3px}
  .card .lines span::before{content:"";width:4px;height:4px;border-radius:50%;background:#fff;flex:none}
  .card .cardtitle{font-family:"Montserrat",sans-serif;font-weight:700;font-size:7px;color:#fff}

  /* Lockup */
  .lockup{left:928px;top:650px;width:252px;height:220px;text-align:center}
  .lockup .mark{font-family:"Lato",sans-serif;font-weight:700;font-size:118px;line-height:120px;color:var(--grey);letter-spacing:4px}
  .lockup .name-top{font-family:"Lato",sans-serif;font-weight:400;font-size:27px;color:var(--red);letter-spacing:.5px;margin-top:10px}
  .lockup .name-bottom{display:flex;align-items:center;gap:6px;font-family:"Lato",sans-serif;font-size:20px;color:var(--grey);letter-spacing:1px;margin-top:2px}
  .lockup .name-bottom::before,.lockup .name-bottom::after{content:"";flex:1;height:2px;background:var(--grey)}
</style>
</head>
<body>

<!-- Booklet cover -->
<section class="piece booklet">
  <svg viewBox="0 0 436 588">
    <defs>
      <linearGradient id="bkPaper" x1="0" y1="0" x2="1" y2="1"><stop offset="0" stop-color="#f4f4f4"/><stop offset="1" stop-color="#ffffff"/></linearGradient>
      <linearGradient id="bkPhoto" x1="0" y1="0" x2="0.4" y2="1"><stop offset="0" stop-color="#dfe3e6"/><stop offset=".55" stop-color="#8d9195"/><stop offset="1" stop-color="#2a2b2d"/></linearGradient>
      <linearGradient id="bkRed" x1="0" y1="0" x2="1" y2="1"><stop offset="0" stop-color="#d8252a"/><stop offset="1" stop-color="#e8383c"/></linearGradient>
    </defs>
    <rect width="436" height="588" fill="url(#bkPaper)"/>
    <path d="M300,0 L436,0 L436,330 C452,170 410,60 300,0Z" fill="#b9babc"/>
    <path d="M0,260 C100,170 300,110 400,140 C440,230 330,420 0,570 Z" fill="url(#bkPhoto)" role="img" aria-label="Photograph of a glass office tower seen from below"/>
    <path d="M0,560 C140,500 320,400 436,250 L436,290 C320,430 150,520 0,588 Z" fill="#9fa1a4"/>
    <path d="M0,588 C150,524 330,430 436,300 L436,588 Z" fill="url(#bkRed)"/>
    <rect x="282" y="480" width="40" height="12" fill="#fff"/>
    <rect x="296" y="466" width="12" height="40" fill="#fff"/>
    <path d="M330,440 l26,0 l6,-8 l4,0 l-3,8 l8,0 l4,-4 l2,0 l-2,5 l2,5 l-2,0 l-4,-4 l-8,0 l3,8 l-4,0 l-6,-8 l-26,0z" fill="#fff"/>
    <path d="M378,440 C420,450 440,490 420,520 C400,560 330,560 300,580" fill="none" stroke="#fff" stroke-opacity=".6" stroke-width="1" stroke-dasharray="3 3"/>
    <rect x="0" y="0" width="10" height="588" fill="#000" opacity=".06"/>
  </svg>
  <div class="abs brand">KTR</div>
  <div class="abs title">COLLABORATION</div>
  <div class="abs tagline">Build your brand, benefit philosophy, &amp; benefit identify</div>
</section>
<div class="label" style="left:240px;top:632px">BOOKLET COVER</div>

<!-- Letterhead -->
<section class="piece letterhead">
  <svg viewBox="0 0 416 588">
    <rect width="416" height="80" fill="var(--red)"/>
    <path d="M0,0 L150,0 C120,50 70,90 0,105 Z" fill="#9c9ea1"/>
    <path d="M0,0 L132,0 C100,52 60,80 0,98 Z" fill="#fff"/>
    <path d="M190,150 L250,150 L250,560 L190,560 Z" fill="#f6f6f6" role="img" aria-label="Faint medical emblem watermark"/>
    <rect y="552" width="416" height="36" fill="var(--red)"/>
  </svg>
  <div class="abs brand">KTR</div>
  <div class="abs contact" style="left:186px;top:20px"><i></i>1-800-555-0142</div>
  <div class="abs contact" style="left:186px;top:40px"><i></i>helpdesk@kestreltrust.example</div>
  <div class="abs contact" style="left:186px;top:60px"><i></i>www.kestreltrust.example</div>
  <div class="abs meta" style="left:20px;top:131px">Your Name Here</div>
  <div class="abs meta" style="left:20px;top:147px;font-size:7px">Address</div>
  <div class="abs meta" style="right:20px;top:121px">Date: 21 Apr, 2018</div>
  <p class="abs body" style="top:184px">Lorem ipsum dolor sit amet, consectetur adipiscing elit. Suspendisse condimentum egestas tellus et viverra. Vestibulum euismod lacus eget nisi ornare, id laoreet tortor dapibus. Donec lacinia euismod diam, convallis tempus risus. Ut et felis tempor eros blandit feugiat ut non enim. In vestibulum ligula blandit magna blandit dictum. Sed malesuada erat id mauris pretium, eget congue felis interdum. Aenean ultricies enim nec lorem vestibulum, nec commodo quam sagittis. Cras bibendum mauris, eget aliquet semper, libero ipsum ultricies nunc, euismod pellentesque orci risus amet nibh. Maecenas feuiat mi a metus convallis pharetra.</p>
  <p class="abs body" style="top:274px">Duis porta turpis ut pulvinar hendrerit elit lorem vehicula turpis, lacinia semper purus ros ac nisi. Sed consectetur ante scelerisque tortor pellentesque imperdiet. Pellentesque habitant morbi tristique senectus et netus et malesuada fames ac turpis egestas. Quisque justo turpis, varius ante nec, tincidunt pharetra tellus. Donec non euismod est. Nulla in elit quis tellus mattis feugiat vitae vitae ut magna. Etiam at nisi quis dolor facilisis hendrerit placerat et risus. Vestibulum ac sapien ut justo varius venenatis.</p>
  <div class="abs meta" style="left:20px;top:415px;font-size:7px">Regards</div>
  <div class="abs meta" style="left:20px;top:477px;font-size:7px">Your Name Here</div>
  <div class="abs meta" style="left:20px;top:487px;font-size:7px">Designation Here</div>
  <div class="abs contact foot"><i></i>48 Harbour Lane, Suite 210 - Box 412, Brightwater, ON, K0L 2B0</div>
</section>
<div class="label" style="left:705px;top:632px">LETTERHEAD</div>

<!-- Health card -->
<section class="piece card health">
  <svg viewBox="0 0 229 138">
    <rect width="229" height="138" fill="#f3f3f3"/>
    <path d="M128,0 L229,0 L229,138 L0,138 C80,126 122,78 128,0Z" fill="var(--red)"/>
    <path d="M114,0 L128,0 C122,78 80,126 0,138 L0,131 C72,118 108,74 114,0Z" fill="#9c9ea1"/>
    <rect x="210" y="8" width="14" height="104" rx="6" fill="#fff" opacity=".8" role="img" aria-label="Medical emblem artwork"/>
  </svg>
  <div class="abs brand" style="left:18px;top:44px">KTR</div>
  <div class="abs sub" style="left:18px;top:82px">KESTREL TRUST</div>
  <div class="abs sub2" style="left:18px;top:91px">—REINSURERS—</div>
  <div class="abs lines" style="left:140px;top:62px">
    <span>48 Harbour Lane, Suite 210 - Box 412,</span>
    <span>Brightwater, ON, K0L 2B0</span>
    <span>1-800-555-0142</span>
    <span>helpdesk@kestreltrust.example</span>
    <span>www.kestreltrust.example</span>
  </div>
  <div class="abs cardtitle" style="left:76px;top:118px">MEDICAL HEALTH BENEFIT CARD</div>
</section>
<div class="label" style="left:1064px;top:183px">HEALTH CARD</div>

<!-- Travel card -->
<section class="piece card travel">
  <svg viewBox="0 0 229 138">
    <rect width="229" height="138" fill="#f3f3f3"/>
    <path d="M128,0 L229,0 L229,138 L0,138 C80,126 122,78 128,0Z" fill="var(--red)"/>
    <path d="M114,0 L128,0 C122,78 80,126 0,138 L0,131 C72,118 108,74 114,0Z" fill="#9c9ea1"/>
    <rect x="210" y="8" width="14" height="98" rx="6" fill="#fff" opacity=".8" role="img" aria-label="Medical emblem artwork"/>
    <path d="M22,40 l14,0 l4,-6 l3,0 l-2,6 l6,0 l3,-3 l2,0 l-2,4 l2,4 l-2,0 l-3,-3 l-6,0 l2,6 l-3,0 l-4,-6 l-14,0z" fill="#9c9ea1"/>
  </svg>
  <div class="abs brand" style="left:18px;top:50px">KTR</div>
  <div class="abs sub" style="left:18px;top:88px">KESTREL TRUST</div>
  <div class="abs sub2" style="left:18px;top:97px">—REINSURERS—</div>
  <div class="abs lines" style="left:140px;top:58px">
    <span>48 Harbour Lane, Suite 210 - Box 412,</span>
    <span>Brightwater, ON, K0L 2B0</span>
    <span>1-800-555-0142</span>
    <span>helpdesk@kestreltrust.example</span>
    <span>www.kestreltrust.example</span>
  </div>
  <div class="abs cardtitle" style="left:80px;top:110px">EMERGENCY MEDICAL TRAVEL CARD</div>
  <div class="abs" style="left:118px;top:121px;font-size:3.8px;color:#fff;font-weight:700">— POLICY : KTR 5520418 —</div>
</section>
<div class="label" style="left:1064px;top:391px">TRAVEL CARD</div>

<!-- Business card front -->
<section class="piece card front">
  <svg viewBox="0 0 229 138">
    <rect width="229" height="138" fill="#f3f3f3"/>
    <path d="M146,0 L229,0 L229,138 L0,138 C90,126 140,76 146,0Z" fill="var(--red)"/>
    <path d="M132,0 L146,0 C140,76 90,126 0,138 L0,131 C82,118 126,72 132,0Z" fill="#9c9ea1"/>
    <rect x="212" y="8" width="12" height="122" rx="5" fill="#fff" opacity=".8" role="img" aria-label="Medical emblem artwork"/>
  </svg>
  <div class="abs brand" style="left:16px;top:44px;font-size:26px">KTR</div>
  <div class="abs sub" style="left:16px;top:79px">KESTREL TRUST</div>
  <div class="abs sub2" style="left:16px;top:88px">—REINSURERS—</div>
  <div class="abs cardtitle" style="left:138px;top:54px;font-size:9.5px">LOREM IPSUM</div>
  <div class="abs" style="left:152px;top:67px;font-size:5px;color:#fff;font-weight:700">Designation Here</div>
  <div class="abs lines" style="left:134px;top:80px">
    <span>48 Harbour Lane, Suite 210 - Box 412,</span>
    <span>Brightwater, ON, K0L 2B0</span>
    <span>1-800-555-0142</span>
    <span>helpdesk@kestreltrust.example</span>
    <span>www.kestreltrust.example</span>
  </div>
</section>
<div class="label" style="left:137px;top:850px">FRONT</div>

<!-- Business card back -->
<section class="piece card back">
  <div class="abs brand" style="left:0;width:229px;text-align:center;top:28px;font-size:46px">KTR</div>
  <div class="abs" style="left:0;width:229px;text-align:center;top:90px;font-size:12px;color:var(--red)">KESTREL TRUST</div>
  <div class="abs" style="left:0;width:229px;text-align:center;top:105px;font-size:9px;color:var(--grey);letter-spacing:1px">—— REINSURERS ——</div>
</section>
<div class="label" style="left:402px;top:850px">BACK</div>

<!-- Logo lockup -->
<section class="abs lockup">
  <div class="mark">KTR</div>
  <div class="name-top">KESTREL TRUST</div>
  <div class="name-bottom">REINSURERS</div>
</section>

</body>
</html>
```